ITSM Book Cover

I need ideas for my new book cover. I currently have 2 possible titles. 1.) The Hands-On Institute of ITSM 2.) ITSM Worth, Honestly Truly! The book covers real life experiences & examples of how to 1.) understand ITSM & 2.) Best practices around implementation. ITSM = Information Technology Service Management. The final design should sell VALUE! I'm a great believer in choice is not about choice it's about value or perceived value. I need to capture this on the cover.

Information Technology

```html
<!DOCTYPE html>
<html lang="en">
<head>
<meta charset="utf-8">
<title>The Hands-On Institute of ITSM — Book Cover</title>
<link rel="stylesheet" href="https://fonts.googleapis.com/css2?family=Rubik+Dirt&family=Tinos&display=swap">
<style>
  :root {
    --ink: #000000;
    --paper: #ffffff;
    --burst-crimson: #6e0f32;
    --burst-teal: #13574a;
    --author-teal: #1d4a40;
    --author-red: #5a1424;
    --row-1: #15b394;
    --row-2: #1a86d8;
    --row-3: #1f5bec;
    --row-4: #2f3ee6;
    --row-5: #4a30d8;
    --row-6: #5d29c6;
    --row-7: #6e22ae;
    --row-8: #7c1f96;
    --row-9: #8a1c7c;
    --row-10: #981a58;
  }
  * { margin: 0; padding: 0; box-sizing: border-box; }
  html, body {
    width: 848px; height: 1200px; overflow: hidden; background: var(--ink);
  }
  .cover {
    position: relative; width: 848px; height: 1200px; overflow: hidden;
    background: var(--ink);
  }
  .burst { position: absolute; pointer-events: none; }
  .burst--crimson-top {
    left: 300px; top: -20px; width: 560px; height: 560px;
    background: radial-gradient(ellipse at 48% 55%, rgba(110,15,50,0.55) 0%, rgba(110,15,50,0.18) 35%, rgba(110,15,50,0) 68%);
  }
  .burst--crimson-edge {
    left: 720px; top: 480px; width: 180px; height: 330px;
    background: radial-gradient(ellipse at 60% 50%, rgba(110,15,50,0.45) 0%, rgba(110,15,50,0) 70%);
  }
  .burst--teal-mid {
    left: -60px; top: 520px; width: 200px; height: 200px;
    background: radial-gradient(ellipse at 40% 50%, rgba(19,87,74,0.5) 0%, rgba(19,87,74,0) 70%);
  }
  .burst--teal-low {
    left: -40px; top: 800px; width: 380px; height: 420px;
    background: radial-gradient(ellipse at 38% 45%, rgba(19,87,74,0.55) 0%, rgba(19,87,74,0.15) 40%, rgba(19,87,74,0) 70%);
  }
  .title {
    position: absolute; left: 104px; top: 78px;
    font-family: "Rubik Dirt", system-ui, sans-serif;
    font-weight: 400; font-size: 46px; line-height: 65px;
    color: var(--paper); text-transform: uppercase; letter-spacing: 1px;
  }
  .title span { display: block; }
  .author {
    position: absolute; left: 162px; top: 494px;
    font-family: "Tinos", serif; font-variant: small-caps;
    font-size: 20px; letter-spacing: 9px;
    background: linear-gradient(90deg, var(--author-teal), var(--author-red));
    -webkit-background-clip: text; background-clip: text; color: transparent;
  }
  .acrostic {
    position: absolute; left: 360px; top: 570px;
    display: flex; font-family: "Tinos", serif;
  }
  .acrostic__column {
    display: flex; flex-direction: column; align-items: center;
  }
  .acrostic__column:nth-child(1) { width: 56px; }
  .acrostic__column:nth-child(2) { width: 56px; margin-left: 46px; }
  .acrostic__column:nth-child(3) { width: 56px; margin-left: 46px; }
  .acrostic__column:nth-child(4) { width: 56px; margin-left: 58px; }
  .acrostic__initial {
    color: var(--paper); font-size: 50px; line-height: 60px; margin-bottom: 40px;
  }
  .acrostic__rest { display: flex; flex-direction: column; align-items: center; }
  .acrostic__rest span { font-size: 20px; line-height: 51px; height: 51px; }
  .acrostic__rest span:nth-child(1) { color: var(--row-1); }
  .acrostic__rest span:nth-child(2) { color: var(--row-2); }
  .acrostic__rest span:nth-child(3) { color: var(--row-3); }
  .acrostic__rest span:nth-child(4) { color: var(--row-4); }
  .acrostic__rest span:nth-child(5) { color: var(--row-5); }
  .acrostic__rest span:nth-child(6) { color: var(--row-6); }
  .acrostic__rest span:nth-child(7) { color: var(--row-7); }
  .acrostic__rest span:nth-child(8) { color: var(--row-8); }
  .acrostic__rest span:nth-child(9) { color: var(--row-9); }
  .acrostic__rest span:nth-child(10) { color: var(--row-10); }
</style>
</head>
<body>
<main class="cover">
  <div class="burst burst--crimson-top" role="img" aria-label="Crimson fractal starburst of crossing light strands"></div>
  <div class="burst burst--crimson-edge" role="img" aria-label="Crimson fractal starburst at the right edge"></div>
  <div class="burst burst--teal-mid" role="img" aria-label="Small teal fractal starburst at the left edge"></div>
  <div class="burst burst--teal-low" role="img" aria-label="Teal fractal starburst of crossing light strands"></div>

  <h1 class="title">
    <span>The</span>
    <span>Hands-On</span>
    <span>Institute</span>
    <span>of</span>
  </h1>

  <p class="author">Author’s Name</p>

  <div class="acrostic" aria-label="ITSM: Information Technology Service Management">
    <div class="acrostic__column">
      <span class="acrostic__initial">I</span>
      <div class="acrostic__rest"><span>N</span><span>F</span><span>O</span><span>R</span><span>M</span><span>A</span><span>T</span><span>I</span><span>O</span><span>N</span></div>
    </div>
    <div class="acrostic__column">
      <span class="acrostic__initial">T</span>
      <div class="acrostic__rest"><span>E</span><span>C</span><span>H</span><span>N</span><span>O</span><span>L</span><span>O</span><span>G</span><span>Y</span></div>
    </div>
    <div class="acrostic__column">
      <span class="acrostic__initial">S</span>
      <div class="acrostic__rest"><span>E</span><span>R</span><span>V</span><span>I</span><span>C</span><span>E</span></div>
    </div>
    <div class="acrostic__column">
      <span class="acrostic__initial">M</span>
      <div class="acrostic__rest"><span>A</span><span>N</span><span>A</span><span>G</span><span>E</span><span>M</span><span>E</span><span>N</span><span>T</span></div>
    </div>
  </div>
</main>
</body>
</html>
```